VELINTA Promotions - Business Card Design Project

We are looking for a classy business cards for Promotion Company based in Toronto, Canada named Velinta Promotions.

Velinta Promotions has an idea and vision to set high standard, be EXCLUSIVE and attract a group of people that will follow us through events we promote (night clubs, brand promotions, music events, and sport events)

We want to present a high standards and classy image to the others...
Updates

Target Market(s)

male/female age 25-40 Target: business owners young entrepreneur - clubing industry - media industry - promotion industry - marketing media industry

Industry/Entity Type

Events

Requirements
Must have
• business cards should be classy, make people feel exclusive , make people react ..

```html
<!DOCTYPE html>
<html lang="en">
<head>
<meta charset="utf-8">
<title>Velinta Promotions – Business Cards</title>
<link href="https://fonts.googleapis.com/css2?family=Arimo:wght@400;700&display=swap" rel="stylesheet">
<style>
  :root {
    --page: #ffffff;
    --aqua: #3ff2e2;
    --aqua-light: #a9fbf4;
    --ink: #111111;
    --night: #0b0b0b;
    --paper-text: #f2f2f2;
    --shadow: rgba(0, 0, 0, 0.45);
  }
  * { margin: 0; padding: 0; box-sizing: border-box; }
  html, body {
    width: 997px;
    height: 1200px;
    overflow: hidden;
    background: var(--page);
  }
  body {
    position: relative;
    font-family: "Arimo", Arial, sans-serif;
  }
  .card {
    position: absolute;
    left: 109px;
    width: 794px;
    height: 458px;
    box-shadow: 10px 12px 14px var(--shadow);
    overflow: hidden;
  }
  .card--front { top: 58px; }
  .card--back { top: 618px; }
  .card__bg { position: absolute; inset: 0; width: 100%; height: 100%; display: block; }
  .card__text { position: absolute; white-space: nowrap; }

  /* front */
  .holder { right: 71px; top: 26px; text-align: right; color: var(--ink); }
  .holder__name { font-size: 25px; letter-spacing: 0.5px; }
  .holder__name strong { font-weight: 700; }
  .holder__role { font-size: 16px; margin-top: 6px; }

  .brand { color: var(--aqua); font-weight: 400; text-align: right; }
  .brand__name { display: block; letter-spacing: 6px; line-height: 1; }
  .brand__tag { display: block; letter-spacing: 9px; line-height: 1; }
  .brand--large { left: 80px; top: 150px; width: 610px; }
  .brand--large .brand__name { font-size: 80px; }
  .brand--large .brand__tag { font-size: 20px; margin-top: 10px; }

  .front-contact { left: 34px; top: 384px; color: var(--ink); font-size: 17px; line-height: 34px; }
  .front-contact strong { font-weight: 700; }

  /* back */
  .services { left: 566px; top: 20px; color: var(--ink); font-size: 16px; line-height: 27px; }
  .services strong { font-weight: 700; }
  .address, .office-contact { color: var(--paper-text); font-size: 18px; line-height: 35.5px; }
  .address { left: 33px; top: 100px; }
  .office-contact { left: 308px; top: 171px; }
  .brand--small { left: 410px; top: 322px; width: 330px; text-align: center; }
  .brand--small .brand__name { font-size: 40px; letter-spacing: 3px; }
  .brand--small .brand__tag { font-size: 11px; letter-spacing: 6px; margin-top: 4px; }
  .web { left: 33px; top: 388px; color: var(--ink); }
  .web__note { font-size: 14px; }
  .web__url { font-size: 18px; font-weight: 700; margin-top: 10px; }
</style>
</head>
<body>

<section class="card card--front">
  <svg class="card__bg" viewBox="0 0 794 458" preserveAspectRatio="none" aria-hidden="true">
    <defs>
      <linearGradient id="glowTop" x1="0" y1="0" x2="0" y2="1">
        <stop offset="0" stop-color="var(--aqua)"/>
        <stop offset="1" stop-color="var(--aqua-light)"/>
      </linearGradient>
      <linearGradient id="glowBottom" x1="0" y1="1" x2="0" y2="0">
        <stop offset="0" stop-color="var(--aqua)"/>
        <stop offset="1" stop-color="var(--aqua-light)"/>
      </linearGradient>
    </defs>
    <rect width="794" height="458" fill="var(--aqua)"/>
    <path d="M0,60 C180,30 330,40 480,95 S690,150 794,128 L794,0 L0,0 Z" fill="url(#glowTop)"/>
    <path d="M0,74 C180,44 330,54 480,109 S690,164 794,142 L794,318 C640,320 520,350 360,370 S120,350 0,316 Z" fill="var(--night)"/>
    <path d="M0,316 C120,350 240,378 360,370 S640,320 794,318 L794,458 L0,458 Z" fill="url(#glowBottom)"/>
  </svg>

  <div class="card__text holder">
    <p class="holder__name">MARCUS <strong>Hale</strong></p>
    <p class="holder__role">Managing Director</p>
  </div>

  <div class="card__text brand brand--large">
    <span class="brand__name">VELINTA</span>
    <span class="brand__tag">PROMOTIONS</span>
  </div>

  <div class="card__text front-contact">
    <p>Telephone: <strong>(0) 4321 8765 09</strong></p>
    <p>Email: <strong>mhale@velintapromotions.co.uk</strong></p>
  </div>
</section>

<section class="card card--back">
  <svg class="card__bg" viewBox="0 0 794 458" preserveAspectRatio="none" aria-hidden="true">
    <defs>
      <linearGradient id="glowTopBack" x1="0" y1="0" x2="0" y2="1">
        <stop offset="0" stop-color="var(--aqua)"/>
        <stop offset="1" stop-color="var(--aqua-light)"/>
      </linearGradient>
      <linearGradient id="glowBottomBack" x1="0" y1="1" x2="0" y2="0">
        <stop offset="0" stop-color="var(--aqua)"/>
        <stop offset="1" stop-color="var(--aqua-light)"/>
      </linearGradient>
    </defs>
    <rect width="794" height="458" fill="var(--aqua)"/>
    <path d="M0,40 C160,14 300,26 440,80 S690,168 794,150 L794,0 L0,0 Z" fill="url(#glowTopBack)"/>
    <path d="M0,54 C160,28 300,40 440,94 S690,182 794,164 L794,352 C660,332 520,322 380,338 S150,350 0,330 Z" fill="var(--night)"/>
    <path d="M0,330 C150,350 260,352 380,338 S660,332 794,352 L794,458 L0,458 Z" fill="url(#glowBottomBack)"/>
  </svg>

  <div class="card__text services">
    <p><strong>Night</strong> Clubs</p>
    <p><strong>Brand</strong> Promotions</p>
    <p><strong>Music</strong> Events</p>
    <p><strong>Sporting</strong> Events</p>
  </div>

  <div class="card__text address">
    <p>Velinta Promotions</p>
    <p>48 Harbour Lane</p>
    <p>York Region</p>
    <p>Toronto</p>
    <p>Zip Code 5821</p>
  </div>

  <div class="card__text office-contact">
    <p>Telephone: 01987 654320</p>
    <p>Fax: 01987 654330</p>
    <p>Email: velintapromotions@mailbox.com</p>
  </div>

  <div class="card__text brand brand--small">
    <span class="brand__name">VELINTA</span>
    <span class="brand__tag">PROMOTIONS</span>
  </div>

  <div class="card__text web">
    <p class="web__note">Visit our website for more information:-</p>
    <p class="web__url">www.velintapromotions.co.ca</p>
  </div>
</section>

</body>
</html>
```